Marrow Vance Fine Art gallery website - Modern british art for sale

We need a website design that is both current and high end. Our products are expensive and this should be reflected in the look of the website. We would like the logo we had designed last year to be clearly seen in the design. We want sleek, simple, and easy to navigate. Nothing too colourful as the colours of the art should always take precedence.

Target Market(s)

The average price of one our products starts at £250 and can go up to £10,000 we are an entry level gallery.

Industry/Entity Type

Art Gallery

Number of Pages Required

5+ page

Font styles to use
Sans Serif

Colors
000000
ffffff
faa54b
abd037
886aae
b868aa

Requirements
Must have
• Attractive front page. Linked to our Twitter feed.
• 4 links from front page - New Releases, about us, Artists, contact us
• Social media links - Facebook, Twitter, YouTube, Instagram.
• Each artist must have their own page, each page must have a biography link to another page.
Nice to have
• Utilise our new logo design. I would like the Twitter feed to link to the front page in a small way so you can see what's being said on Twitter by the company. For future proofing maybe have a locations function on the front page which can be adroit down menu showing where our other galleries are.

```html
<!DOCTYPE html>
<html lang="en">
<head>
<meta charset="utf-8">
<title>Marrow Vance Fine Art</title>
<link rel="stylesheet" href="https://fonts.googleapis.com/css2?family=Montserrat:wght@400;600;700&family=Oswald:wght@400;500&display=swap">
<style>
:root{
  --green:#8ba83a;
  --green-dark:#6f8a2a;
  --white:#ffffff;
  --ink:#1f1f1f;
  --grey:#777777;
  --pale:#f0f2e6;
  --about-bg:#2a2a2a;
  --artists-bg:#1f1f1b;
  --contact-bg:#eeeee8;
  --line:#d8d8cf;
  --art-warm:#d9a27a;
  --art-warm-2:#b98fb0;
  --art-ink:#8a8a8a;
  --art-ink-2:#d9d9d9;
  --art-cool:#6f86a8;
  --art-cool-2:#c9b56a;
  --art-stone:#8e9a96;
  --art-stone-2:#b4b6b0;
}
*{margin:0;padding:0;box-sizing:border-box}
html,body{width:1200px;height:3220px;overflow:hidden}
body{font-family:"Montserrat",sans-serif;color:var(--ink);background:var(--white);position:relative}
.abs{position:absolute}
.heading{position:absolute;left:0;width:1200px;display:flex;justify-content:center;align-items:center;gap:14px;font-family:"Oswald",sans-serif;font-weight:500;font-size:34px;letter-spacing:0.5px;text-transform:uppercase;white-space:nowrap}
.heading::before,.heading::after{content:"";display:block;width:92px;height:3px;background:var(--green)}
.heading--light{color:var(--white)}
.heading--start{justify-content:flex-start;left:185px;width:auto}

/* Hero */
.hero{position:absolute;left:0;top:0;width:1200px;height:522px;background:linear-gradient(120deg,#3a3a3a 0%,#5b4a48 30%,#8c5a52 48%,#2e3b48 62%,#4f6f7f 78%,#6b6b66 100%)}
.hero__shade{position:absolute;inset:0;background:linear-gradient(180deg,rgba(0,0,0,.55) 0%,rgba(0,0,0,.2) 60%,rgba(0,0,0,.35) 100%)}
.brand{position:absolute;left:183px;top:44px;color:var(--white);font-size:26px;font-weight:400;line-height:1.1;width:230px}
.nav{position:absolute;left:488px;top:55px;display:flex;gap:40px;font-size:12px;letter-spacing:1.2px;color:#d6d6d6;text-transform:uppercase;white-space:nowrap}
.nav a{color:inherit;text-decoration:none}
.nav .is-active{color:var(--white);font-weight:700}
.social{position:absolute;display:flex;gap:8px}
.social span{display:block;width:24px;height:24px;border-radius:3px;background:var(--white)}
.hero .social{left:934px;top:13px}
.hero__title{position:absolute;left:183px;top:174px;color:var(--white);font-size:32px;font-weight:600;letter-spacing:2px;white-space:nowrap}
.hero__intro{position:absolute;left:183px;top:248px;width:560px;color:#e8e8e8;font-size:16px;line-height:27px;letter-spacing:1.4px}

/* About */
.about{position:absolute;left:0;top:522px;width:1200px;height:455px;background:var(--about-bg)}
.about .heading{top:26px}
.about__copy{position:absolute;left:397px;top:108px;width:365px;color:#d0d0d0;font-size:11.5px;line-height:21px}
.about__copy strong{display:block;color:var(--white);font-size:14px;line-height:22px;font-weight:600;margin-bottom:14px}
.about__copy p{margin-bottom:16px}
.tweets{position:absolute;left:790px;top:111px;width:223px;height:265px;background:#f3f3f3;border:2px solid #cfcfcf;border-radius:3px;overflow:hidden;font-size:9px;color:#333}
.tweets__head{display:flex;justify-content:space-between;align-items:center;height:26px;padding:0 6px;background:#e6e6e6;border-bottom:1px solid #cfcfcf}
.tweets__head b{font-size:12px}
.tweets__follow{background:#dadada;border:1px solid #bbb;border-radius:3px;padding:2px 5px;font-size:8px}
.tweet{display:flex;gap:6px;padding:8px 6px;border-bottom:1px solid #dcdcdc;height:70px}
.tweet__avatar{flex:none;width:34px;height:34px;background:#bdbdbd}
.tweet__body{flex:1;line-height:12px}
.tweet__time{float:right;color:#999}
.tweet__handle{color:#888}
.tweet__text{color:#777;margin-top:3px}
.tweets__box{position:absolute;left:4px;right:4px;bottom:4px;height:22px;background:var(--white);border:1px solid #ccc;padding:5px;color:#888;font-size:9px}

/* New releases */
.releases{position:absolute;left:0;top:977px;width:1200px;height:1073px;background:var(--pale)}
.releases .heading{top:34px;color:var(--ink)}
.releases__intro{position:absolute;left:193px;top:104px;width:820px;text-align:center;color:var(--grey);font-size:13px;line-height:22px}
.card{position:absolute;width:257px}
.card__art{width:257px;height:232px;background:var(--white);padding:12px;box-shadow:0 1px 4px rgba(0,0,0,.15)}
.card__art div{width:100%;height:100%}
.card__title{margin-top:17px;font-family:"Oswald",sans-serif;font-size:12px;font-weight:500;text-transform:uppercase;color:var(--ink);white-space:nowrap;letter-spacing:-0.1px}
.card__text{margin-top:6px;font-size:14px;line-height:22px;color:var(--grey)}
.card__price{margin-top:16px;font-size:15px;font-weight:700}
.btn{position:absolute;display:flex;align-items:center;justify-content:center;background:var(--green);color:var(--white);font-family:"Oswald",sans-serif;font-size:13px;text-transform:uppercase;box-shadow:0 2px 0 var(--green-dark)}

/* Artists */
.artists{position:absolute;left:0;top:2050px;width:1200px;height:591px;background:var(--artists-bg)}
.artists .heading{top:50px}
.artist{position:absolute;width:405px;color:var(--white)}
.artist__name{font-size:15px;font-weight:600;letter-spacing:.5px}
.artist__bio{margin-top:14px;font-size:11.5px;line-height:21px;color:#cfcfcf}
.btn-outline{display:inline-flex;align-items:center;justify-content:center;margin-top:29px;width:111px;height:29px;border:2px solid var(--green);color:var(--white);font-family:"Oswald",sans-serif;font-size:13px;text-transform:uppercase}

/* Contact */
.contact{position:absolute;left:0;top:2641px;width:1200px;height:515px;background:var(--contact-bg)}
.contact .heading{top:26px}
.contact__item{position:absolute;left:183px;display:flex;gap:26px;align-items:flex-start;color:var(--grey);font-size:12.5px;line-height:22px}
.contact__item svg{flex:none}
.field{position:absolute;border-bottom:1px solid var(--green);color:#b5b5b5;font-size:10px;padding-bottom:6px}
.field--area{border:2px solid var(--green);padding:6px}
.map{position:absolute;left:640px;top:90px;width:373px;height:376px;background:linear-gradient(135deg,#e9e4d6 0%,#d8e4ec 100%);border:6px solid var(--white);box-shadow:0 1px 4px rgba(0,0,0,.15)}

/* Footer */
.footer{position:absolute;left:0;top:3156px;width:1200px;height:64px;background:var(--contact-bg);border-top:1px solid var(--line)}
.footer__copy{position:absolute;left:183px;top:27px;font-size:9px;color:#444}
.footer__follow{position:absolute;left:880px;top:27px;font-size:9px;font-family:"Oswald",sans-serif;color:#444;text-transform:uppercase}
.footer .social{left:930px;top:20px}
.footer .social span{background:#555;width:22px;height:22px}
</style>
</head>
<body>

<header class="hero">
  <div class="hero__shade" role="img" aria-label="Photograph of an abstract painted wall with an ornate street lamp"></div>
  <div class="brand">Marrow Vance Fine Art</div>
  <nav class="nav">
    <a class="is-active" href="#">Home</a>
    <a href="#about">About us</a>
    <a href="#releases">New releases</a>
    <a href="#artists">Artists</a>
    <a href="#contact">Contact us</a>
  </nav>
  <div class="social" aria-label="Social media links"><span></span><span></span><span></span></div>
  <h1 class="hero__title">Welcome to Marrow Vance Fine Art</h1>
  <p class="hero__intro">We've been on the web since our information in the year 2000 and in our 10th Year of Business we find an ever progressing internet demanding another change in our Website. We hope that you like what we've done.</p>
</header>

<section class="about" id="about" role="region" aria-label="About us">
  <h2 class="heading heading--light heading--start">About us</h2>
  <div class="about__copy">
    <strong>Lorem ipsum dolor sit amet, ei dicit persius molestiae usu, vide soluta everttitur e</strong>
    <p>I has, ei vix debet philosophia. Viris nullam sententiae mel id. Eu bonorum eruditi voluptatibus est, ipsum quodsi discere id his. Has at primis reprehendunt, ex sit ludus habemus maluisset, mea id illud quidam salutatus.</p>
    <p>At invenire salutatus sed, consequuntur reprehendunt an vis. Cum meis laudem id, postulant democritum voluptaria cu quo, has at illud sonet dictas. Menandri deserunt delicatissimi ad eam. Nam at summo decore, eu modus viviendo maluisset vix.</p>
  </div>
  <aside class="tweets" aria-label="Twitter feed">
    <div class="tweets__head"><b>Tweets</b><span class="tweets__follow">Follow @marrowvancefa</span></div>
    <div class="tweet"><div class="tweet__avatar"></div><div class="tweet__body"><span class="tweet__time">2h</span><b>Marrow Vance Fine Art</b><br><span class="tweet__handle">@marrowvancefa</span><div class="tweet__text">New prints have just landed in the gallery, come and see them.</div></div></div>
    <div class="tweet"><div class="tweet__avatar"></div><div class="tweet__body"><span class="tweet__time">5h</span><b>Marrow Vance Fine Art</b><br><span class="tweet__handle">@marrowvancefa</span><div class="tweet__text">Thank you to everyone who joined our late opening last night.</div></div></div>
    <div class="tweet"><div class="tweet__avatar"></div><div class="tweet__body"><span class="tweet__time">1d</span><b>Marrow Vance Fine Art</b><br><span class="tweet__handle">@marrowvancefa</span><div class="tweet__text">Our winter catalogue is out now, browse the latest releases online.</div></div></div>
    <div class="tweets__box">Tweet to @marrowvancefa</div>
  </aside>
</section>

<section class="releases" id="releases" role="region" aria-label="New releases">
  <h2 class="heading">New releases</h2>
  <p class="releases__intro">At invenire salutatus sed, consequuntur reprehendunt an vis. Cum meis laudem id, postulant democritum voluptaria cu quo, has at illud sonet dictas. Menandri deserunt delicatissimi ad eam. Nam at summo decore, eu modus viviendo maluisset vix.</p>

  <article class="card" style="left:187px;top:197px">
    <div class="card__art"><div role="img" aria-label="Artwork: colourful abstract print" style="background:linear-gradient(180deg,var(--art-warm),var(--art-warm-2))"></div></div>
    <h3 class="card__title">At invenire salutatus sed, consequuntur reat</h3>
    <p class="card__text">Menandri deserunt delicatissimi ad eam. Nam at summo decore, eu m</p>
    <p class="card__price">£250</p>
  </article>
  <article class="card" style="left:472px;top:197px">
    <div class="card__art"><div role="img" aria-label="Artwork: ink drawing of a city building" style="background:linear-gradient(180deg,var(--art-ink-2),var(--art-ink))"></div></div>
    <h3 class="card__title">At invenire salutatus sed, consequuntur reat</h3>
    <p class="card__text">Menandri deserunt delicatissimi ad eam. Nam at summo decore, eu m</p>
    <p class="card__price">£5000</p>
  </article>
  <article class="card" style="left:756px;top:197px">
    <div class="card__art"><div role="img" aria-label="Artwork: black and white line drawing" style="background:linear-gradient(180deg,var(--art-ink-2),var(--art-ink))"></div></div>
    <h3 class="card__title">At invenire salutatus sed, consequuntur reat</h3>
    <p class="card__text">Menandri deserunt delicatissimi ad eam. Nam at summo decore, eu m</p>
    <p class="card__price">£10,000</p>
  </article>

  <article class="card" style="left:187px;top:597px">
    <div class="card__art"><div role="img" aria-label="Artwork: black and white line drawing" style="background:linear-gradient(180deg,var(--art-ink-2),var(--art-ink))"></div></div>
    <h3 class="card__title">At invenire salutatus sed, consequuntur reat</h3>
    <p class="card__text">Menandri deserunt delicatissimi ad eam. Nam at summo decore, eu m</p>
    <p class="card__price">£250</p>
  </article>
  <article class="card" style="left:472px;top:597px">
    <div class="card__art"><div role="img" aria-label="Artwork: geometric colour print" style="background:linear-gradient(180deg,var(--art-cool),var(--art-cool-2))"></div></div>
    <h3 class="card__title">At invenire salutatus sed, consequuntur reat</h3>
    <p class="card__text">Menandri deserunt delicatissimi ad eam. Nam at summo decore, eu m</p>
    <p class="card__price">£5000</p>
  </article>
  <article class="card" style="left:756px;top:597px">
    <div class="card__art"><div role="img" aria-label="Artwork: muted abstract painting" style="background:linear-gradient(180deg,var(--art-stone),var(--art-stone-2))"></div></div>
    <h3 class="card__title">At invenire salutatus sed, consequuntur reat</h3>
    <p class="card__text">Menandri deserunt delicatissimi ad eam. Nam at summo decore, eu m</p>
    <p class="card__price">£10,000</p>
  </article>

  <a class="btn" style="left:537px;top:994px;width:126px;height:43px">See more</a>
</section>

<section class="artists" id="artists" role="region" aria-label="Artists">
  <div class="abs" style="inset:0;background:linear-gradient(180deg,#24241f,#1a1a17)" role="img" aria-label="Dark photograph of city rooftops"></div>
  <h2 class="heading heading--light">Artists</h2>
  <div class="artist" style="left:183px;top:130px">
    <h3 class="artist__name">Ada Thornfield</h3>
    <p class="artist__bio">Has, ei vix debet philosophia. Viris nullam sententiae mel id. Eu bonorum eruditi voluptatibus est, ipsum quodsi discere id his. Has at primis reprehendunt, ex sit ludus habemus maluisset, mea id illud quidam salutatus.</p>
    <a class="btn-outline">Learn more</a>
  </div>
  <div class="artist" style="left:612px;top:130px">
    <h3 class="artist__name">Felix Marlowe</h3>
    <p class="artist__bio">Has, ei vix debet philosophia. Viris nullam sententiae mel id. Eu bonorum eruditi voluptatibus est, ipsum quodsi discere id his. Has at primis reprehendunt, ex sit ludus habemus maluisset, mea id illud quidam salutatus.</p>
    <a class="btn-outline">Learn more</a>
  </div>
  <div class="artist" style="left:183px;top:349px">
    <h3 class="artist__name">Jonah Brightwell</h3>
    <p class="artist__bio">Has, ei vix debet philosophia. Viris nullam sententiae mel id. Eu bonorum eruditi voluptatibus est, ipsum quodsi discere id his. Has at primis reprehendunt, ex sit ludus habemus maluisset, mea id illud quidam salutatus.</p>
    <a class="btn-outline">Learn more</a>
  </div>
  <div class="artist" style="left:612px;top:349px">
    <h3 class="artist__name">Ewan Halloway</h3>
    <p class="artist__bio">Has, ei vix debet philosophia. Viris nullam sententiae mel id. Eu bonorum eruditi voluptatibus est, ipsum quodsi discere id his. Has at primis reprehendunt, ex sit ludus habemus maluisset, mea id illud quidam salutatus.</p>
    <a class="btn-outline">Learn more</a>
  </div>
</section>

<section class="contact" id="contact" role="region" aria-label="Contact us">
  <h2 class="heading">Contact us</h2>
  <div class="contact__item" style="top:88px">
    <svg width="20" height="26" viewBox="0 0 20 26"><path d="M10 0C4.5 0 0 4.4 0 9.8 0 17 10 26 10 26s10-9 10-16.2C20 4.4 15.5 0 10 0z" fill="#8ba83a"/><circle cx="10" cy="9.5" r="3.5" fill="#eeeee8"/></svg>
    <p>Vas, ei vix debet philosophia.<br>Viris nullam sententiae mel id. Eu bonorum eruditi</p>
  </div>
  <div class="contact__item" style="top:155px">
    <svg width="22" height="22" viewBox="0 0 22 22"><path d="M5 1l4 5-2.5 2.5c1.2 2.8 3.3 4.9 6 6L15 12l5 4-2 4.5C9 21 1 13 1.5 3z" fill="#8ba83a"/></svg>
    <p>(123) 555-0142</p>
  </div>
  <div class="contact__item" style="top:208px">
    <svg width="30" height="22" viewBox="0 0 30 22"><rect x="0" y="0" width="30" height="22" fill="#8ba83a"/><path d="M1 1l14 11L29 1" stroke="#eeeee8" stroke-width="2" fill="none"/></svg>
    <p>hello@marrowvancefa.example</p>
  </div>
  <div class="field" style="left:183px;top:288px;width:193px">Name</div>
  <div class="field" style="left:397px;top:288px;width:189px">Email</div>
  <div class="field field--area" style="left:183px;top:326px;width:403px;height:82px">Your Message</div>
  <a class="btn" style="left:183px;top:429px;width:128px;height:43px">Send</a>
  <div class="map" role="img" aria-label="Street map showing the gallery location"></div>
</section>

<footer class="footer">
  <p class="footer__copy">© Copyright 2017 Marrow Vance Fine Art. All rights reserved.</p>
  <span class="footer__follow">Follow us</span>
  <div class="social" aria-label="Social media links"><span></span><span></span><span></span></div>
</footer>

</body>
</html>
```